Postcard design to acquire new clients for my Property Management Company

I'm looking for a postcard design that I can send to prospective clients detailing information about my company and services.
Postcard should be eye catching and contain information from www.brightkeyrentals-example.com. I've provided a few screen shots for the most important information and my logo.
Target Market(s)
Real Estate
Industry/Entity Type
Real Estate
Font styles to use
Sans Serif
Requirements
Must have
- Must be eye catching!! this will be a direct mail piece - I'd like for the card to be read and not tossed in the trash immediately.
Design que from the logo.
A place to write / print the receipts name and address.
our physical address - 2287 Marble Lane, Lubbock, TX 79555.
Should not have
- the contact information on the business card is not accurate - please use info from website.

```html
<!DOCTYPE html>
<html lang="en">
<head>
<meta charset="utf-8">
<title>BrightKey Property Management – Postcard</title>
<link href="https://fonts.googleapis.com/css2?family=Montserrat:ital,wght@0,400;0,500;0,600;0,700;1,300;1,400&family=Arimo:ital@1&display=swap" rel="stylesheet">
<style>
  :root {
    --bg: #2b2c2e;
    --blue: #0f4d8a;
    --grey: #808080;
    --light: #efefef;
    --white: #ffffff;
    --ink: #1b1b1b;
    --rule: #8c8c8c;
  }
  * { margin: 0; padding: 0; box-sizing: border-box; }
  html, body { width: 1071px; height: 1200px; overflow: hidden; background: var(--bg); }
  body { position: relative; font-family: "Montserrat", sans-serif; }

  .card { position: absolute; width: 610px; height: 406px; overflow: hidden; background: var(--white); }
  .card-front { left: 151px; top: 171px; }
  .card-back { left: 313px; top: 633px; }

  /* Front */
  .front-photo {
    position: absolute; inset: 0;
    background: linear-gradient(100deg, #c9c4bc 0%, #dcd8d1 35%, #b9aca0 65%, #9c7d6c 100%);
  }
  .brand-box {
    position: absolute; left: 0; top: 0; width: 214px; height: 71px;
    background: var(--white);
    clip-path: polygon(0 0, 100% 0, 88% 100%, 0 100%);
  }
  .brand-name {
    position: absolute; left: 20px; top: 20px; color: var(--blue);
    font-weight: 600; line-height: 1;
  }
  .brand-name .main { display: block; font-size: 19px; letter-spacing: 2.4px; }
  .brand-name .sub { display: block; font-size: 8.2px; letter-spacing: 1.6px; margin-top: 4px; }

  .front-band {
    position: absolute; left: 185px; top: 332px; width: 425px; height: 74px;
    background: var(--blue);
    clip-path: polygon(26px 0, 100% 0, 100% 100%, 0 100%);
  }
  .front-headline {
    position: absolute; right: 15px; top: 13px; color: var(--white);
    font-weight: 700; font-size: 14.6px; letter-spacing: -0.1px; white-space: nowrap;
    text-decoration: underline; text-decoration-thickness: 1px; text-underline-offset: 3px;
  }
  .front-tagline {
    position: absolute; right: 15px; top: 35px; color: var(--white); white-space: nowrap;
    font-family: "Arimo", sans-serif; font-style: italic; font-size: 10.3px;
  }
  .front-url {
    position: absolute; left: 414px; top: 383px; width: 196px; height: 23px;
    background: var(--white);
    clip-path: polygon(10px 0, 100% 0, 100% 100%, 0 100%);
    color: var(--blue); font-weight: 700; font-size: 8.6px; white-space: nowrap;
    display: flex; align-items: center; justify-content: flex-end; padding-right: 15px;
  }

  /* Back */
  .back-shapes { position: absolute; inset: 0; }
  .services-title {
    position: absolute; left: 27px; top: 27px; color: var(--white);
    font-weight: 700; font-size: 22.5px; letter-spacing: -0.2px; white-space: nowrap;
  }
  .services-intro {
    position: absolute; left: 27px; top: 54px; color: var(--white); white-space: nowrap;
    font-family: "Arimo", sans-serif; font-style: italic; font-size: 12.3px;
  }
  .service-list {
    position: absolute; left: 31px; top: 114px; list-style: none; color: var(--white);
  }
  .service-list li {
    display: flex; align-items: center; height: 21.4px; white-space: nowrap;
    font-style: italic; font-weight: 300; font-size: 16.5px;
  }
  .service-list svg { width: 15px; height: 15px; margin-right: 10px; fill: var(--white); flex: none; }

  .contact-phone {
    position: absolute; left: 28px; top: 330px; color: var(--white); white-space: nowrap;
    font-weight: 700; font-size: 21.5px; letter-spacing: -0.3px; line-height: 1;
  }
  .contact-url {
    position: absolute; left: 28px; top: 357px; color: var(--white); white-space: nowrap;
    font-weight: 600; font-size: 8.2px; line-height: 1;
  }
  .contact-address {
    position: absolute; left: 28px; top: 371px; color: var(--white); white-space: nowrap;
    font-weight: 500; font-size: 8.2px; line-height: 1;
  }

  .stamp-box {
    position: absolute; left: 498px; top: 35px; width: 72px; height: 71px;
    border: 1px solid #9a9a9a; background: var(--white);
  }
  .to-label { position: absolute; left: 347px; top: 148px; color: var(--ink); font-weight: 700; font-size: 11px; }
  .address-line { position: absolute; left: 347px; width: 223px; height: 1px; background: var(--rule); }
</style>
</head>
<body>

<section class="card card-front">
  <div class="front-photo" role="img" aria-label="Photo of a smiling property manager handing house keys to a couple in a bright apartment"></div>
  <div class="brand-box">
    <div class="brand-name"><span class="main">BRIGHTKEY</span><span class="sub">PROPERTY MANAGEMENT</span></div>
  </div>
  <div class="front-band">
    <p class="front-headline">PROPERTY MANAGEMENT ACROSS LUBBOCK, TX</p>
    <p class="front-tagline">Maximize your financial returns with support from our rental specialists</p>
  </div>
  <div class="front-url">www.brightkeyrentals-example.com</div>
</section>

<section class="card card-back">
  <svg class="back-shapes" width="610" height="406" viewBox="0 0 610 406">
    <rect width="610" height="406" fill="var(--white)"/>
    <polygon points="372,0 455,0 290,406 208,406" fill="var(--light)"/>
    <polygon points="0,0 372,0 336,91 0,91" fill="var(--blue)"/>
    <polygon points="0,91 342,91 250,322 0,322" fill="var(--grey)"/>
    <polygon points="0,322 247,322 208,406 0,406" fill="var(--blue)"/>
  </svg>

  <h2 class="services-title">DISCOVER OUR SERVICES</h2>
  <p class="services-intro">We offer full-service property management solutions</p>

  <ul class="service-list">
    <li><svg viewBox="0 0 16 16"><path d="M8 1 0 8h2v7h4v-4h4v4h4V8h2z"/></svg>Property Marketing</li>
    <li><svg viewBox="0 0 16 16"><circle cx="5" cy="5" r="3"/><circle cx="11.5" cy="5.5" r="2.5"/><path d="M0 14c0-3 2-5 5-5s5 2 5 5zM10.5 14c0-2-.6-3.5-1.6-4.4.8-.4 1.6-.6 2.6-.6 2.5 0 4.5 2 4.5 5z"/></svg>Tenant Screening</li>
    <li><svg viewBox="0 0 16 16"><path d="M7 0h2v2c2 .3 3.5 1.5 3.5 3.5h-2.3c0-1-.9-1.6-2.2-1.6S5.8 4.4 5.8 5.300c0 1 .9 1.3 2.6 1.7 2.3.5 4.3 1.2 4.3 3.8 0 2-1.5 3.2-3.7 3.5V16H7v-1.7c-2.3-.3-3.8-1.7-3.8-3.8h2.3c0 1.2 1 1.9 2.6 1.9 1.4 0 2.3-.6 2.3-1.5 0-1-.8-1.300-2.7-1.7C5.6 8.7 3.5 8 3.5 5.5 3.5 3.6 5 2.3 7 2z"/></svg>Rent Collection</li>
    <li><svg viewBox="0 0 16 16"><path d="M7 2l4-1 4 4-2 2-2-2-9 10-2-2 10-9z"/></svg>Maintenance</li>
    <li><svg viewBox="0 0 16 16"><path d="M6.5 1a5.5 5.5 0 0 1 4.4 8.8l4.6 4.6-1.4 1.4-4.6-4.6A5.5 5.5 0 1 1 6.5 1zm0 2a3.5 3.5 0 1 0 0 7 3.5 3.5 0 0 0 0-7z"/></svg>Property Inspections</li>
    <li><svg viewBox="0 0 16 16"><path d="M1 2h1.5v11H15v1.5H1z"/><path d="M4 8h1.5v4H4zM7 5h1.5v7H7zM10 7h1.5v5H10zM13 4h1.5v8H13z"/></svg>Financial Reporting</li>
    <li><svg viewBox="0 0 16 16"><path d="M8 0 1.5 2.5V7c0 4.5 3 7.8 6.5 9 3.5-1.2 6.5-4.5 6.5-9V2.5zm0 2v12c-2.5-1-4.5-3.7-4.5-7V3.8z"/></svg>Evictions</li>
    <li><svg viewBox="0 0 16 16"><path d="M7.3 1h1.4v2H14v1.4h-1.2l2.2 5.6c0 1.4-1.3 2.5-3 2.5s-3-1.1-3-2.5l2.2-5.6H8.7V13H12v1.5H4V13h3.3V4.4H4.8L7 10c0 1.4-1.3 2.5-3 2.5S1 11.4 1 10l2.2-5.6H2V3h5.3zM4 6 2.5 9.6h3zm8 0-1.5 3.6h3z"/></svg>Legal Guidance</li>
  </ul>

  <p class="contact-phone">(806)555-0142</p>
  <p class="contact-url">WWW.BRIGHTKEYRENTALS-EXAMPLE.COM</p>
  <p class="contact-address">2287 Marble Lane, Lubbock, TX 79555</p>

  <div class="stamp-box"></div>
  <p class="to-label">TO</p>
  <div class="address-line" style="top:192px"></div>
  <div class="address-line" style="top:228px"></div>
  <div class="address-line" style="top:261px"></div>
  <div class="address-line" style="top:297px"></div>
</section>

</body>
</html>
```